Invitation card for birthday of 10-year old

Design a birthday part invitation card for a 10-year old. The card should have a musical theme (the birthday girl is a pianist and vocalist).
Here is one of her social media pages: www.example-social.com/melodyfinchstage.
There are many images/videos of her here -- please include a picture of her from this page on the card.

The text for the card is:

LET'S PARTY (in large font)

JOIN US TO CELEBRATE
LINNEA'S 10th BIRTHDAY

482 BRAMBLECREST WAY, OAKVEND NJ 08163
2pm--6pm

```html
<!DOCTYPE html>
<html lang="en">
<head>
<meta charset="utf-8">
<title>Linnea's 10th Birthday Invitation</title>
<link rel="stylesheet" href="https://fonts.googleapis.com/css2?family=Sniglet:wght@800&family=Arimo:wght@400&display=swap">
<style>
  :root {
    --card-pink: #f28ac0;
    --title-white: #ffffff;
    --title-edge: #e05fa6;
    --ink: #111111;
    --photo-top: #8a8a90;
    --photo-bottom: #d9c7cf;
    --key-black: #0d0d0d;
    --key-white: #ffffff;
    --notes-top: #f7b5d6;
    --notes-bottom: #e98dbb;
  }
  * { margin: 0; padding: 0; box-sizing: border-box; }
  html, body { width: 857px; height: 1200px; overflow: hidden; background: var(--card-pink); }
  .invitation {
    position: relative;
    width: 857px;
    height: 1200px;
    background: var(--card-pink);
    font-family: "Arimo", Arial, sans-serif;
    overflow: hidden;
  }
  .headline {
    position: absolute;
    top: 22px;
    left: 0;
    width: 100%;
    text-align: center;
    font-family: "Sniglet", "Arial Rounded MT Bold", sans-serif;
    font-weight: 800;
    font-size: 112px;
    letter-spacing: 3px;
    color: var(--title-white);
    -webkit-text-stroke: 2px var(--title-edge);
    paint-order: stroke fill;
  }
  .portrait {
    position: absolute;
    left: 163px;
    top: 180px;
    width: 531px;
    height: 611px;
    clip-path: polygon(25% 0, 75% 0, 100% 22%, 100% 78%, 75% 100%, 25% 100%, 0 78%, 0 22%);
    background: linear-gradient(180deg, var(--photo-top), var(--photo-bottom));
  }
  .celebrate {
    position: absolute;
    top: 812px;
    left: 0;
    width: 100%;
    text-align: center;
    color: var(--ink);
    font-size: 50px;
    line-height: 62px;
    text-transform: uppercase;
  }
  .celebrate .age {
    font-family: "Sniglet", "Arial Rounded MT Bold", sans-serif;
    font-weight: 800;
    color: var(--title-white);
    text-transform: none;
    font-size: 48px;
  }
  .address {
    position: absolute;
    top: 985px;
    left: 0;
    width: 100%;
    text-align: center;
    color: var(--title-white);
    font-size: 33px;
  }
  .hours {
    position: absolute;
    top: 1046px;
    left: 0;
    width: 100%;
    text-align: center;
    color: var(--title-white);
    font-size: 31px;
  }
  .keyboard-band {
    position: absolute;
    left: 0;
    bottom: 0;
    width: 857px;
    height: 64px;
  }
  .music-staff {
    position: absolute;
    left: 285px;
    top: 1085px;
    width: 330px;
    height: 100px;
    background: linear-gradient(180deg, var(--notes-top), var(--notes-bottom));
  }
</style>
</head>
<body>
<main class="invitation">
  <h1 class="headline">LET'S PARTY</h1>

  <div class="portrait" role="img" aria-label="Photo of the birthday girl, Linnea, smiling and reaching toward the camera on stage"></div>

  <p class="celebrate">Join us to celebrate<br>Linnea's <span class="age">10th</span> birthday</p>

  <p class="address">482 BRAMBLECREST WAY, OAKVEND NJ 08163</p>
  <p class="hours">2pm-6pm</p>

  <svg class="keyboard-band" viewBox="0 0 857 64" aria-hidden="true">
    <rect x="0" y="0" width="857" height="64" fill="var(--key-white)"/>
    <g fill="var(--key-black)">
      <rect x="0" y="0" width="24" height="64"/>
      <rect x="45" y="0" width="24" height="64"/>
      <rect x="90" y="0" width="24" height="64"/>
      <rect x="135" y="0" width="24" height="64"/>
      <rect x="180" y="0" width="24" height="64"/>
      <rect x="225" y="0" width="24" height="64"/>
      <rect x="270" y="0" width="24" height="64"/>
      <rect x="315" y="0" width="24" height="64"/>
      <rect x="360" y="0" width="24" height="64"/>
      <rect x="405" y="0" width="24" height="64"/>
      <rect x="450" y="0" width="24" height="64"/>
      <rect x="495" y="0" width="24" height="64"/>
      <rect x="540" y="0" width="24" height="64"/>
      <rect x="585" y="0" width="24" height="64"/>
      <rect x="630" y="0" width="24" height="64"/>
      <rect x="675" y="0" width="24" height="64"/>
      <rect x="720" y="0" width="24" height="64"/>
      <rect x="765" y="0" width="24" height="64"/>
      <rect x="810" y="0" width="24" height="64"/>
    </g>
  </svg>

  <div class="music-staff" role="img" aria-label="Illustration of a treble clef and musical notes on a staff"></div>
</main>
</body>
</html>
```